Tidal Fern Business Cards

We need something new, fun and exciting for business cards. Our current ones are just plain and we need a design that pops. We want name, position held, phone, email on the front, and a 20% discount on the back. I have also uploaded our old business cards creative to see what we are not wanting, and how boring they were and we want something jazzed up from this, cool design and catches people attention.

```html
<!DOCTYPE html>
<html lang="en">
<head>
<meta charset="utf-8">
<title>Tidal Fern Business Cards</title>
<link rel="stylesheet" href="https://fonts.googleapis.com/css2?family=Montserrat:wght@600;700;800&family=Open+Sans:wght@400&display=swap">
<style>
  :root {
    --navy: #1c3d6e;
    --coral: #f07370;
    --white: #ffffff;
    --paper: #ffffff;
    --stage: #c8c8c8;
    --ink-soft: #4f4f4f;
    --shadow: rgba(0, 0, 0, 0.28);
  }
  * { margin: 0; padding: 0; box-sizing: border-box; }
  html, body {
    width: 1200px;
    height: 1000px;
    overflow: hidden;
    background: var(--stage);
  }
  .card {
    position: absolute;
    left: 234px;
    width: 732px;
    height: 417px;
    box-shadow: 0 3px 8px var(--shadow);
    overflow: hidden;
  }
  .card--offer { top: 75px; background: var(--navy); }
  .card--contact { top: 508px; background: var(--paper); }

  .brand {
    position: absolute;
    display: flex;
    align-items: center;
    font-family: "Montserrat", sans-serif;
    font-weight: 600;
    letter-spacing: -1px;
    white-space: nowrap;
  }
  .brand__dot {
    border-radius: 50%;
    background: var(--coral);
    flex: none;
  }
  .card--offer .brand {
    left: 92px;
    top: 110px;
    font-size: 72px;
    color: var(--white);
    gap: 26px;
  }
  .card--offer .brand__dot { width: 54px; height: 54px; }
  .card--contact .brand {
    left: 38px;
    top: 52px;
    font-size: 46px;
    color: var(--navy);
    gap: 18px;
  }
  .card--contact .brand__dot { width: 34px; height: 34px; }

  .offer {
    position: absolute;
    left: 180px;
    top: 282px;
    display: flex;
    align-items: baseline;
    gap: 14px;
    font-family: "Montserrat", sans-serif;
    white-space: nowrap;
  }
  .offer__value { font-weight: 800; font-size: 72px; color: var(--coral); letter-spacing: -1px; }
  .offer__label { font-weight: 700; font-size: 32px; color: var(--white); }

  .address, .contacts {
    position: absolute;
    left: 39px;
    font-family: "Open Sans", sans-serif;
    font-size: 19px;
    color: var(--ink-soft);
    line-height: 26.5px;
    list-style: none;
  }
  .address { top: 167px; font-style: normal; }
  .contacts { top: 252px; left: 38px; }
  .contacts li { display: flex; align-items: center; gap: 6px; }
  .contacts svg { width: 16px; height: 16px; fill: var(--coral); flex: none; }

  .person {
    position: absolute;
    right: 39px;
    top: 166px;
    text-align: right;
  }
  .person__name {
    font-family: "Montserrat", sans-serif;
    font-weight: 700;
    font-size: 25px;
    color: var(--navy);
    line-height: 32px;
  }
  .person__first { color: var(--coral); }
  .person__role {
    font-family: "Open Sans", sans-serif;
    font-size: 18px;
    color: var(--ink-soft);
    line-height: 24px;
  }
  .wave { position: absolute; left: 0; top: 0; width: 732px; height: 417px; }
</style>
</head>
<body>
  <section class="card card--offer">
    <div class="brand"><span class="brand__dot"></span>TidalFern</div>
    <p class="offer"><span class="offer__value">20%</span><span class="offer__label">DISCOUNT</span></p>
  </section>

  <section class="card card--contact">
    <svg class="wave" viewBox="0 0 732 417" aria-hidden="true">
      <path d="M0,360 Q330,420 732,322 L732,417 L0,417 Z" fill="var(--navy)"/>
      <path d="M0,331 Q200,395 700,326 Q330,405 0,356 Z" fill="var(--coral)"/>
    </svg>
    <div class="brand"><span class="brand__dot"></span>TidalFern</div>
    <address class="address">2715 W. Harbor Ln<br>Portland, OR 97201</address>
    <ul class="contacts">
      <li><svg viewBox="0 0 16 16"><path d="M3.5 1.5l2.3 2.6-1.2 1.8c.9 2 2.5 3.6 4.5 4.5l1.8-1.2 2.6 2.3-1.3 2.6C6.9 13.8 2.2 9.1 1 3z"/></svg>(555) 014-2286</li>
      <li><svg viewBox="0 0 16 16"><path d="M1 3.5h14v9H1z M1.6 4l6.4 5 6.4-5" stroke="var(--white)" stroke-width="1"/></svg>hello@tidalfern.com</li>
      <li><svg viewBox="0 0 16 16"><circle cx="8" cy="8" r="7"/><path d="M1 8h14M8 1c3 3 3 11 0 14M8 1c-3 3-3 11 0 14" stroke="var(--white)" stroke-width="1" fill="none"/></svg>www.tidalfern.com</li>
    </ul>
    <div class="person">
      <p class="person__name"><span class="person__first">MARINA</span> HOLT</p>
      <p class="person__role">Founder &amp; CEO</p>
    </div>
  </section>
</body>
</html>
```